Voucher Postcard Design

We need a postcard that will act as a gift card for our restaurants located in Charlotte N.C. These will be used to give out when we want to offer a special thank you or in lieu of "comping" a meal as a means to get the customer to come back with a meal on us.
We are a owner operated restaurant specializing in Southern American cuisine. Always made from scratch with the finest ingredients.
We offer Breakfast, Brunch,Lunch and DInner - Meadowlark Café offers a unique and exceptional dining experience, with an eclectic menu and inviting atmosphere. We are known for our Red Velvet Waffles and artisan coffees. We would like to see the colors green, yellow and brown used in the design. Attached is a ad that reflects these colors. We would need to include a dollar amount of $10 that reflects the value of the card.

Industry/Entity Type

Restaurant

Requirements
Must have
• Would like to include the photo of the red velvet waffle.
Must have the $10 amount indicating the value of the card.
Disclosure: not valid with any other offers, discounts, or promotional meal deals. One coupon per visit, per table. no cash value. excludes purchase of gift cards. Valid for dine in only.

```html
<!DOCTYPE html>
<html lang="en">
<head>
<meta charset="utf-8">
<title>Meadowlark Café – $10 Voucher</title>
<link href="https://fonts.googleapis.com/css2?family=Roboto+Condensed:ital,wght@0,400;0,700;1,400;1,700&display=swap" rel="stylesheet">
<style>
  :root {
    --cream: #f5f1ee;
    --blush: #e6b3b5;
    --berry: #c23a44;
    --deep-red: #9e1a26;
    --band-red: #c8282c;
    --cocoa: #5b3a2c;
    --cocoa-dark: #4a2c20;
    --leaf: #6fb52c;
    --ink: #111111;
    --white: #ffffff;
  }
  html, body {
    margin: 0;
    padding: 0;
    overflow: hidden;
    background: var(--white);
  }
  .voucher {
    position: relative;
    width: 1200px;
    height: 930px;
    overflow: hidden;
    font-family: "Roboto Condensed", "Arial Narrow", sans-serif;
  }
  .hero-photo {
    position: absolute;
    inset: 0;
    background:
      radial-gradient(ellipse 420px 380px at 1010px 260px, #d8202e 0%, rgba(200,30,45,0.85) 45%, rgba(200,30,45,0) 100%),
      linear-gradient(100deg, var(--cream) 0%, #f1e3e1 28%, var(--blush) 45%, var(--berry) 72%, var(--deep-red) 100%);
  }
  .brand {
    position: absolute;
    left: 29px;
    top: 48px;
    display: flex;
    align-items: center;
    gap: 12px;
  }
  .brand-dot {
    width: 26px;
    height: 26px;
    border-radius: 50%;
    background: var(--leaf);
  }
  .brand-name {
    font-size: 40px;
    font-weight: 700;
    color: var(--leaf);
    line-height: 1;
  }
  .locations {
    position: absolute;
    left: 61px;
    top: 154px;
    font-size: 18px;
    font-weight: 700;
    color: var(--band-red);
    letter-spacing: 0.2px;
  }
  .headline {
    position: absolute;
    left: 59px;
    top: 236px;
    margin: 0;
    font-size: 74px;
    font-weight: 700;
    line-height: 82px;
    color: var(--ink);
    letter-spacing: -0.5px;
  }
  .website {
    position: absolute;
    left: 61px;
    top: 600px;
    font-size: 16px;
    font-weight: 700;
    color: var(--ink);
  }
  .value-badge {
    position: absolute;
    left: 880px;
    top: 78px;
    width: 240px;
    height: 254px;
  }
  .caption-band {
    position: absolute;
    left: 0;
    top: 780px;
    width: 1200px;
    height: 32px;
    background: var(--band-red);
    color: var(--white);
    font-size: 18px;
    font-weight: 700;
    text-align: right;
    box-sizing: border-box;
    padding: 8px 31px 0 0;
    line-height: 1;
  }
  .disclosure-band {
    position: absolute;
    left: 0;
    top: 812px;
    width: 1200px;
    height: 118px;
    background: var(--cocoa);
    color: var(--white);
    box-sizing: border-box;
    padding: 28px 30px 0 59px;
    font-size: 27px;
    font-style: italic;
    line-height: 33px;
    white-space: nowrap;
  }
  .disclosure-band strong { font-weight: 700; }
</style>
</head>
<body>
<main class="voucher">
  <div class="hero-photo" role="img" aria-label="Close-up photo of red velvet waffles dusted with powdered sugar, drizzled with cream icing and topped with a fresh strawberry"></div>

  <div class="brand">
    <span class="brand-dot"></span>
    <span class="brand-name">Meadowlark Café</span>
  </div>

  <div class="locations">WILLOWBROOK - CEDAR HILL</div>

  <h1 class="headline">Distinctive American<br>Southern Cuisine for<br>Breakfast, Lunch<br>and Dinner.</h1>

  <div class="website">www.meadowlarkcafecharlotte.com</div>

  <svg class="value-badge" viewBox="0 0 240 254" aria-label="$10 value">
    <polygon points="-25,112 60,112 60,165 -25,165 -8,138" fill="var(--cocoa)"/>
    <polygon points="265,112 180,112 180,165 265,165 248,138" fill="var(--cocoa)"/>
    <ellipse cx="122" cy="127" rx="84" ry="126" fill="var(--cocoa-dark)"/>
    <ellipse cx="122" cy="127" rx="77" ry="119" fill="var(--white)"/>
    <ellipse cx="122" cy="127" rx="71" ry="113" fill="none" stroke="var(--cocoa)" stroke-width="2"/>
    <text x="68" y="134" font-family="Roboto Condensed, sans-serif" font-size="34" fill="var(--cocoa)">$</text>
    <text x="95" y="151" font-family="Roboto Condensed, sans-serif" font-weight="700" font-size="74" fill="var(--cocoa)">10</text>
    <text x="122" y="184" text-anchor="middle" font-family="Roboto Condensed, sans-serif" font-size="34" fill="var(--cocoa)">VALUE</text>
  </svg>

  <div class="caption-band">Red Velvet Waffles</div>

  <div class="disclosure-band">
    <strong>Disclosure:</strong> not valid with any other offers, discounts, or promotional meal deals. One coupon per visit,<br>
    per table. no cash value. excludes purchase of gift cards. Valid for dine in only.
  </div>
</main>
</body>
</html>
```